Complete Website Redesign

We need a complete revamp of our website. Need to add interactive custmer catalog seection tools. Need to add customer spec input for recommended product search results. Need a cutomer lead and opportunity contact capability. Need a complete Branding message revamp. Primary visuals will be prodcut pictures and case studies.
Industrial Customers in the high durability Air movement and fan/blower space; high durability enclosure and flow industries ie. mining, chamicals, manufacturing, water treatment, chemical in use manufacturing

```html
<!DOCTYPE html>
<html lang="en">
<head>
<meta charset="utf-8">
<title>Duraflow Composites – Request Information</title>
<link href="https://fonts.googleapis.com/css2?family=Open+Sans:wght@400;600;700&family=Marcellus&display=swap" rel="stylesheet">
<style>
  :root{
    --brand-blue:#1f2d8f;
    --link-blue:#2a3aa0;
    --accent-red:#8b1a1a;
    --text:#555555;
    --nav-text:#444444;
    --field-bg:#f5f5f5;
    --field-line:#d9d9d9;
    --panel-dark:#2d2a2e;
    --footer-dark:#2d2a2e;
    --footer-deep:#1d1b1e;
    --box-dark:#1f1d20;
    --btn-blue:#2b86c5;
    --btn-steel:#3b73b5;
    --btn-red:#8e0f0f;
    --btn-sage:#7f9a90;
    --orange:#f08a1c;
  }
  *{box-sizing:border-box;margin:0;padding:0}
  html,body{width:1200px;height:1000px;overflow:hidden;background:#fff}
  body{position:relative;font-family:"Open Sans",Arial,sans-serif;color:var(--text)}
  .abs{position:absolute}
  .top-rule{left:0;top:0;width:1200px;height:6px;background:var(--brand-blue)}
  .brand{left:56px;top:22px;display:flex;align-items:center;gap:10px;color:var(--brand-blue)}
  .brand-mark{width:40px;height:40px;background:var(--brand-blue)}
  .brand-name{font-size:17px;font-weight:600;line-height:1.2}
  .brand-name b{display:block;font-size:30px;font-weight:600;line-height:1}
  .call{left:536px;top:14px;font-size:20px;font-weight:600;color:#333;letter-spacing:.5px}
  .call span{color:var(--accent-red)}
  .account{left:1028px;top:19px;font-size:11.5px;color:var(--link-blue);letter-spacing:.5px}
  .account i{font-style:normal;margin:0 9px}
  .nav{top:66px;font-size:11px;color:var(--nav-text);letter-spacing:.6px;text-transform:uppercase}
  .nav.active{color:var(--link-blue)}
  .nav-underline{left:932px;top:83px;width:54px;height:1px;background:var(--link-blue)}
  .header-line{left:35px;top:94px;width:1117px;height:1px;background:#e2e2e2}
  .hero{left:40px;top:95px;width:1106px;height:254px;background:linear-gradient(#f9f9f9,#e3e3e3)}
  .hero-products{left:140px;top:110px;width:900px;height:180px;border-radius:6px;background:linear-gradient(90deg,#8f94a6,#aeb2bf 40%,#9da1ad 70%,#c3c6cf)}
  .tagline{left:40px;top:293px;width:1106px;text-align:center;font-family:"Marcellus",serif;font-size:18.5px;line-height:25px;color:#333;letter-spacing:.6px}
  .selector-shadow{left:104px;top:421px;width:970px;height:22px;background:linear-gradient(#9b9b9b,#cfcfcf)}
  .selector{left:78px;top:349px;width:1024px;height:72px;background:var(--panel-dark)}
  .selector-label{left:241px;top:366px;font-size:17px;font-weight:600;color:#fff}
  .selector-input{left:427px;top:363px;width:424px;height:27px;background:#1d1b1e;border:1px solid #4b484c}
  .btn{display:flex;align-items:center;justify-content:center;color:#fff;font-size:12px;font-weight:600}
  .selector-btn{left:863px;top:366px;width:76px;height:23px;border-radius:5px;background:var(--btn-sage)}
  .selector-note{left:326px;top:400px;font-size:11px;font-weight:600;color:var(--orange)}
  .section-rule{top:493px;height:1px;background:#d0d0d0}
  .section-title{left:470px;top:482px;font-size:18px;color:var(--accent-red);letter-spacing:.5px}
  .col-divider{top:508px;width:1px;height:276px;background:#e6e6e6}
  .label{font-size:15px;color:var(--text)}
  .field{height:22px;background:var(--field-bg);border:1px solid var(--field-line)}
  .select{display:flex;align-items:center;font-size:11px;color:#666}
  .select .caret{position:absolute;right:0;top:0;width:21px;height:20px;background:#a9a9a9}
  .select .caret svg{display:block;margin:6px auto}
  .footer{left:0;top:835px;width:1200px;height:140px;background:var(--footer-dark)}
  .footer-bar{left:0;top:975px;width:1200px;height:25px;background:var(--footer-deep);color:#bbb;font-size:9px;text-align:center;line-height:23px}
  .foot-title{top:840px;font-size:13.5px;font-weight:600;color:#fff;text-align:center;width:200px}
  .quote{left:73px;top:862px;width:196px;height:80px;border-radius:10px;background:#111;color:#fff;font-size:9.5px;line-height:12.6px;padding:9px 10px;text-align:justify}
  .quote em{font-style:normal;color:#e02020}
  .quote-tail{left:160px;top:940px}
  .quote-author{left:210px;top:953px;font-size:11px;color:#fff}
  .social{width:32px;height:32px;border-radius:6px}
  .foot-box{top:868px;height:107px;border-radius:8px 8px 0 0;background:var(--box-dark)}
  .foot-field{background:#3a373b;color:#9a979b;font-size:11px;padding:2px 8px;line-height:16px}
  .foot-btn{height:17px;font-size:12px;font-weight:600;color:#fff;display:flex;align-items:center;justify-content:center}
</style>
</head>
<body>
  <div class="abs top-rule"></div>

  <header>
    <div class="abs brand">
      <div class="brand-mark"></div>
      <div class="brand-name"><b>DFC</b>Duraflow Composites, LLC</div>
    </div>
    <div class="abs call"><span>CALL US :</span> +1 (800) 555 0142</div>
    <div class="abs account">LOGIN<i>|</i>SIGNUP</div>
    <nav>
      <div class="abs nav" style="left:534px">Home</div>
      <div class="abs nav" style="left:610px">Products</div>
      <div class="abs nav" style="left:682px;top:64px">↓</div>
      <div class="abs nav" style="left:712px">About Us</div>
      <div class="abs nav" style="left:810px">Mission</div>
      <div class="abs nav active" style="left:896px">Request Information</div>
      <div class="abs nav" style="left:1066px">Contacts</div>
      <div class="abs nav-underline"></div>
    </nav>
    <div class="abs header-line"></div>
  </header>

  <section>
    <div class="abs hero"></div>
    <div class="abs hero-products" role="img" aria-label="Lineup of fiberglass axial fan, centrifugal blower, roof exhauster and louvered ventilator"></div>
    <p class="abs tagline">WE HAVE A WIDE SELECION OF FIBERGLASS FANS AND OTHER CORROSION RESISTANT AIR HANDLING<br>SOLUTIONS FOR OEMS, CONTRACTORS AND PLANT MAINTENANCE OPERATIONS.</p>
    <div class="abs selector-shadow"></div>
    <div class="abs selector"></div>
    <div class="abs selector-label">PRODUCT SELECTION</div>
    <div class="abs selector-input"></div>
    <div class="abs btn selector-btn">Submit</div>
    <div class="abs selector-note">To verify a catalog number and access product information, enter the complete number (including dashes) above.</div>
  </section>

  <section>
    <div class="abs section-rule" style="left:40px;width:428px"></div>
    <div class="abs section-rule" style="left:700px;width:446px"></div>
    <h2 class="abs section-title" style="font-weight:400">REQUEST INFORMATION</h2>
    <div class="abs col-divider" style="left:415px"></div>
    <div class="abs col-divider" style="left:844px"></div>

    <div class="abs label" style="left:52px;top:569px">Name :</div>
    <div class="abs field" style="left:136px;top:569px;width:255px"></div>
    <div class="abs label" style="left:52px;top:615px">Company :</div>
    <div class="abs field" style="left:136px;top:614px;width:255px"></div>
    <div class="abs label" style="left:52px;top:661px">Title :</div>
    <div class="abs field" style="left:135px;top:661px;width:255px"></div>
    <div class="abs label" style="left:52px;top:706px">Email :</div>
    <div class="abs field" style="left:135px;top:705px;width:255px"></div>

    <div class="abs label" style="left:442px;top:569px">Address 1 :</div>
    <div class="abs field" style="left:569px;top:569px;width:256px"></div>
    <div class="abs label" style="left:442px;top:615px">Address 2 :</div>
    <div class="abs field" style="left:569px;top:614px;width:256px"></div>
    <div class="abs label" style="left:442px;top:661px">City :</div>
    <div class="abs field" style="left:570px;top:661px;width:256px"></div>
    <div class="abs label" style="left:442px;top:706px">State :</div>
    <div class="abs field select" style="left:493px;top:705px;width:128px;padding-left:7px">Choose the state
      <span class="caret"><svg width="10" height="9"><path d="M0 0h10L5 9z" fill="#fff"/></svg></span></div>
    <div class="abs label" style="left:657px;top:706px">Zip :</div>
    <div class="abs field" style="left:706px;top:705px;width:119px"></div>
    <div class="abs label" style="left:442px;top:752px">Phone :</div>
    <div class="abs field" style="left:500px;top:750px;width:128px"></div>
    <div class="abs label" style="left:656px;top:752px">Fax :</div>
    <div class="abs field" style="left:705px;top:750px;width:120px"></div>

    <div class="abs label" style="left:865px;top:569px">How would you like us to contact you?</div>
    <div class="abs field select" style="left:864px;top:593px;width:256px;padding-left:18px">--------------- &nbsp;Please Select &nbsp;-------------
      <span class="caret"><svg width="10" height="9"><path d="M0 0h10L5 9z" fill="#fff"/></svg></span></div>
    <div class="abs label" style="left:865px;top:623px">How may we help you?</div>
    <div class="abs field" style="left:864px;top:650px;width:256px;height:102px"></div>
    <div class="abs btn" style="left:985px;top:759px;width:61px;height:24px;background:linear-gradient(#333,#000)">Clear</div>
    <div class="abs btn" style="left:1054px;top:759px;width:61px;height:24px;background:var(--btn-blue)">Submit</div>
  </section>

  <footer>
    <div class="abs footer"></div>

    <div class="abs foot-title" style="left:63px">TESTIMONIALS</div>
    <div class="abs quote">I have been very satisfied with all of the service provided by <em>DFC</em>. All of your personnel are really focused and were so courteous and professional acting.</div>
    <svg class="abs quote-tail" width="45" height="28"><path d="M0 0h40l4 26z" fill="#111"/></svg>
    <div class="abs quote-author">Mr. Dunn</div>

    <div class="abs foot-title" style="left:314px;top:845px">FOLLOW US</div>
    <div class="abs social" style="left:342px;top:874px;background:#2aa3dc"></div>
    <div class="abs social" style="left:380px;top:874px;background:#d4342a"></div>
    <div class="abs social" style="left:417px;top:874px;background:#3b5a9a"></div>
    <div class="abs social" style="left:454px;top:874px;background:#1c7bb5"></div>
    <div class="abs social" style="left:342px;top:916px;background:#c9222a"></div>
    <div class="abs social" style="left:380px;top:916px;background:#3aa33a"></div>
    <div class="abs social" style="left:418px;top:916px;background:#ef7d1f"></div>

    <div class="abs foot-title" style="left:577px;top:845px">NEWSLETTER</div>
    <div class="abs foot-box" style="left:565px;width:235px"></div>
    <div class="abs foot-field" style="left:587px;top:880px;width:194px;height:20px">Your Name</div>
    <div class="abs foot-field" style="left:587px;top:908px;width:194px;height:20px">Your Email</div>
    <div class="abs foot-btn" style="left:728px;top:953px;width:52px;background:var(--btn-red)">Submit</div>

    <div class="abs foot-title" style="left:872px;top:846px">QUICK CONACT</div>
    <div class="abs foot-box" style="left:858px;width:236px"></div>
    <div class="abs foot-field" style="left:876px;top:881px;width:194px;height:20px">Your Email</div>
    <div class="abs foot-field" style="left:876px;top:909px;width:195px;height:40px">Your Message</div>
    <div class="abs foot-btn" style="left:956px;top:954px;width:53px;background:var(--btn-steel)">Reset</div>
    <div class="abs foot-btn" style="left:1017px;top:954px;width:53px;background:var(--btn-red)">Submit</div>

    <div class="abs footer-bar">Copyright © &nbsp;DFC &nbsp;2013. All rights reserved.</div>
  </footer>
</body>
</html>
```